Dialysis Brochure

12 pages booklet, horizontal, 9 inches width x 6 inches high , luxury look
Updates

Landscape booklet 9 x 6

Need extra days to review

Target Market(s)

General public

Industry/Entity Type

Health Care

Colors

Designer to choose colors to be used in the design.

Requirements
Nice to have
• foil effect or similar

```html
<!DOCTYPE html>
<html lang="en">
<head>
<meta charset="utf-8">
<title>Dialysis Brochure Spread</title>
<link href="https://fonts.googleapis.com/css2?family=Montserrat:wght@400;500;600;700&display=swap" rel="stylesheet">
<style>
  :root {
    --bg: #e2e2e2;
    --paper: #ffffff;
    --paper-soft: #f4f4f5;
    --blue: #2a97d2;
    --magenta: #c8236f;
    --ink: #3b3d42;
    --ink-soft: #6a6d73;
    --photo-light: #e9ecef;
    --photo-mid: #c3c8ce;
  }
  * { box-sizing: border-box; margin: 0; padding: 0; }
  html, body { width: 1200px; height: 840px; overflow: hidden; background: var(--bg); }
  body { font-family: "Montserrat", sans-serif; position: relative; }

  .spread {
    position: absolute; left: 40px; top: 233px;
    width: 1120px; height: 374px;
    display: flex;
    box-shadow: 0 18px 40px rgba(0,0,0,.18);
  }
  .page { position: relative; width: 560px; height: 374px; background: var(--paper); overflow: hidden; }
  .page--left { background: var(--paper-soft); }

  .marker { position: absolute; width: 20px; height: 20px; background: var(--blue); }
  .marker-line { position: absolute; width: 2px; background: var(--blue); }

  .shift-list { position: absolute; left: 70px; top: 92px; list-style: none; }
  .shift-list li { margin-bottom: 14px; }
  .shift-title { font-weight: 700; font-size: 12.5px; letter-spacing: .06em; color: var(--ink); text-transform: uppercase; }
  .shift-title::before { content: "• "; }
  .shift-note { font-size: 10.5px; color: var(--ink-soft); padding-left: 12px; line-height: 1.35; }

  .photo { position: absolute; }
  .photo--clinic-room { left: 290px; top: 0; width: 270px; height: 342px;
    background: linear-gradient(160deg, var(--photo-light) 0%, #d5d9de 45%, var(--photo-mid) 100%); }
  .photo--treatment { left: 300px; top: 18px; width: 242px; height: 338px;
    background: linear-gradient(150deg, #eef0f2 0%, #d6dade 50%, #b9bec4 100%); }

  .contact-band {
    position: absolute; left: 0; bottom: 14px; width: 560px; height: 18px;
    background: var(--magenta); color: #fff; font-size: 9.5px; font-weight: 600;
    letter-spacing: .04em; display: flex; align-items: center; padding-left: 24px;
  }

  .services-panel {
    position: absolute; left: 0; top: 0; width: 300px; height: 342px;
    background: var(--blue); color: #fff; padding: 98px 30px 0 32px;
  }
  .services-title { font-weight: 700; font-size: 13px; letter-spacing: .06em; text-transform: uppercase; margin-bottom: 12px; }
  .services-list { list-style: none; font-size: 11px; line-height: 1.4; }
  .services-list li { margin-bottom: 6px; }
  .services-list li::before { content: "• "; }

  .facility-band {
    position: absolute; left: 0; bottom: 14px; width: 300px; height: 18px;
    background: var(--magenta); color: #fff; font-size: 8.5px; font-weight: 500;
    letter-spacing: .03em; display: flex; align-items: center; justify-content: flex-end; padding-right: 14px;
    text-transform: uppercase;
  }
</style>
</head>
<body>
  <main class="spread">
    <section class="page page--left">
      <span class="marker-line" style="left:55px; top:14px; height:40px;"></span>
      <span class="marker" style="left:46px; top:52px;"></span>
      <ul class="shift-list">
        <li><p class="shift-title">Regular Shifts</p>
            <p class="shift-note">(Monday/Wednesday/Friday or<br>Tuesday/Thursday/Saturday)</p></li>
        <li><p class="shift-title">Early Morning Shifts</p>
            <p class="shift-note">(as early as 5AM)</p></li>
        <li><p class="shift-title">Late Afternoon Shifts</p>
            <p class="shift-note">(after 5PM)</p></li>
      </ul>
      <div class="photo photo--clinic-room" role="img" aria-label="Photo of a bright dialysis treatment room with chairs, machines and wall monitors"></div>
      <div class="contact-band">Ph: (555) 204-7730 | E: info@harborkidney.com</div>
    </section>

    <section class="page page--right">
      <div class="services-panel">
        <span class="marker-line" style="left:52px; top:14px; height:40px; background:#fff;"></span>
        <span class="marker" style="left:43px; top:52px; background:#fff;"></span>
        <h2 class="services-title">Doctor's Services</h2>
        <ul class="services-list">
          <li>Full time Nephrology staff physician on premises</li>
          <li>11 Board Certified Nephrologists</li>
          <li>or YOU MAY KEEP YOUR CURRENT NEPHROLOGIST when you transfer to our Center</li>
        </ul>
      </div>
      <div class="photo photo--treatment" role="img" aria-label="Photo of a patient seated in a dialysis chair while a clinician adjusts the machine"></div>
      <div class="facility-band">Harbor Kidney Care Center Dialysis Facility</div>
    </section>
  </main>
</body>
</html>
```